Brenford Automotive business card
Business card design for Brenford Automotive
Project: Brenford Automotive business card
Brenford Automotive business card - Automotive
Creative Brief
Simple
Wade Pelling
482 Kettle Lane Madison, WI 53790
brenautoco@mailnest.example
Hours: Mon-Thurs 7am-6pm
I want a simple road map on the back of the card, with the business location indicated with a star. The map should include Hwy 37, Hwy 21-29, Quarry Bend Rd, Larkfield Loop / Denholm St, Trobek Rd, Kettle Ln, and Corvell Rd.

```html
<!DOCTYPE html>
<html lang="en">
<head>
<meta charset="utf-8">
<title>Brenford Automotive business card</title>
<link rel="stylesheet" href="https://fonts.googleapis.com/css2?family=Arimo:wght@400;700&display=swap">
<style>
  :root {
    --page-bg: #ece8e2;
    --card-bg: #ffffff;
    --card-edge: #f1f2f4;
    --brand-blue: #1f7cc4;
    --band-blue-dark: #14609f;
    --band-blue-light: #5cb1ea;
    --ink-dark: #3b3d40;
    --ink-text: #55585c;
    --ink-line: #111111;
  }
  html, body {
    margin: 0;
    width: 1200px;
    height: 965px;
    overflow: hidden;
    background: var(--page-bg);
    font-family: "Arimo", Arial, sans-serif;
  }
  .business-card {
    position: absolute;
    left: 100px;
    top: 196px;
    width: 1000px;
    height: 572px;
    border-radius: 42px;
    overflow: hidden;
    background: linear-gradient(180deg, var(--card-bg) 0%, var(--card-bg) 70%, var(--card-edge) 100%);
    box-shadow: 0 6px 18px rgba(0,0,0,0.18);
  }
  .side-band {
    position: absolute;
    left: 0;
    top: 0;
    width: 1000px;
    height: 572px;
  }
  .brand-name {
    position: absolute;
    left: 100px;
    top: 215px;
    width: 330px;
    margin: 0;
    text-align: center;
    font-weight: 700;
    font-size: 46px;
    line-height: 1.1;
    color: var(--ink-dark);
  }
  .contact {
    position: absolute;
    left: 475px;
    top: 120px;
    width: 480px;
    color: var(--ink-text);
  }
  .contact-name {
    margin: 0 0 22px;
    font-size: 32px;
    font-weight: 400;
    color: var(--brand-blue);
  }
  .contact-address {
    margin: 0 0 24px 8px;
    font-style: normal;
    font-size: 21px;
    line-height: 30px;
  }
  .contact-line {
    display: flex;
    align-items: center;
    gap: 8px;
    margin: 0 0 4px 8px;
    font-size: 21px;
    line-height: 32px;
    white-space: nowrap;
  }
  .contact-line svg { flex: none; }
</style>
</head>
<body>
  <div class="business-card">
    <svg class="side-band" viewBox="0 0 1000 572" aria-hidden="true">
      <defs>
        <linearGradient id="bandFill" x1="0" y1="0" x2="1" y2="0">
          <stop offset="0" stop-color="var(--band-blue-dark)"/>
          <stop offset="1" stop-color="var(--band-blue-light)"/>
        </linearGradient>
      </defs>
      <path d="M0 0 H30 C18 200 50 420 140 572 H0 Z" fill="url(#bandFill)"/>
      <path d="M30 0 C18 200 50 420 140 572" fill="none" stroke="var(--ink-line)" stroke-width="6"/>
    </svg>

    <p class="brand-name">Brenford<br>Automotive</p>

    <div class="contact">
      <h1 class="contact-name">Wade Pelling</h1>
      <address class="contact-address">482 Kettle Lane<br>Madison, WI 53790</address>
      <p class="contact-line">
        <svg width="20" height="20" viewBox="0 0 24 24" aria-label="Phone">
          <path d="M6 3 C3 6 4 12 9 17 C13 21 18 22 21 19 L18 15 L15 17 C12 15 9 12 7 9 L9 6 Z" fill="var(--brand-blue)"/>
        </svg>
        (608) 555-0143
      </p>
      <p class="contact-line">
        <svg width="20" height="20" viewBox="0 0 24 24" aria-label="Email">
          <circle cx="12" cy="12" r="4.5" fill="none" stroke="var(--brand-blue)" stroke-width="2.5"/>
          <path d="M16.5 8 V14 C16.5 17 21 17 21 12 A9 9 0 1 0 16 20" fill="none" stroke="var(--brand-blue)" stroke-width="2.5"/>
        </svg>
        brenautoco@mailnest.example
      </p>
    </div>
  </div>
</body>
</html>
```